Palm leaf Plates label design and logo

Hello,
My companies name is Quorvel Tech. My company selling goods on Trodela in different categories. So I have few sub brands. So this time I need a packaging for palm leaf plates which is a product from Velmorani which is one of a subbrand of Quorvel(my main brand). When I was creating a Velmorani brand I was thinking to sell ecological, biodegradable and sustainable products which will prevent Earth from further pollution. So right now I need a well and pretty designed packaging which is basically a label (The label size is 5.5” by 3”(inches)) for palm leaf plates. I attached the word document with all text which should be included. In the middle of the document I included different icons which I would like also to see in the packaging ( obviously not exactly the same, should have unique design as these icons are from my competitors). Also I included PDF document with the barcode. This barcode should be placed on the packaging! It is up to you where you want to place it. The background should be green or brown which would some how linked to a palm or may be you will come up with something even better. I also attached some examples from competitors so you will know what approximately I am looking for. Also I want you to design a logo which would reflect my subbrand nature (Velmorani) It should look modern, fancy and green. I am not going to restrict you with that. Please do your best to come up with logo and also I want you to put logo on the label. In the word document I marked the place where I want to see the logo.

Target Market(s)

Everyone who enjoys green solutions and want make this world greenier

Industry/Entity Type

It Company

Colors

Designer to choose colors to be used in the design.

```html
<!DOCTYPE html>
<html lang="en">
<head>
<meta charset="utf-8">
<title>Velmorani Deluxe Palm Leaf Plates Label</title>
<link href="https://fonts.googleapis.com/css2?family=Barlow+Semi+Condensed:wght@500;600&family=Varela+Round&family=Barlow:wght@600&display=swap" rel="stylesheet">
<style>
  :root {
    --jungle-dark: #173a3c;
    --jungle-mid: #2f6b62;
    --jungle-light: #5fe0b4;
    --wood-light: #ecd7a6;
    --wood-mid: #dcc08a;
    --ink: #2b4b4b;
    --leaf-green: #2e6b4f;
    --badge-fill: #e3cf9a;
    --badge-line: #4f9a6a;
  }
  * { margin: 0; padding: 0; box-sizing: border-box; }
  html, body { width: 1200px; height: 677px; overflow: hidden; }
  body { position: relative; background: var(--jungle-dark); }
  .foliage-backdrop {
    position: absolute; inset: 0;
    background: radial-gradient(circle at 95% 15%, var(--jungle-light) 0%, var(--jungle-mid) 22%, var(--jungle-dark) 55%),
                linear-gradient(160deg, var(--jungle-mid), var(--jungle-dark));
  }
  .label-card {
    position: absolute; left: 84px; top: 0; width: 1032px; height: 635px;
    background: linear-gradient(100deg, var(--wood-light) 0%, var(--wood-mid) 55%, var(--wood-light) 100%);
    color: var(--ink);
  }
  .brand-name {
    position: absolute; left: 34px; top: 48px;
    font-family: "Varela Round", sans-serif; font-size: 84px; letter-spacing: 4px;
    color: var(--ink); text-transform: uppercase; line-height: 1;
  }
  .brand-parent {
    position: absolute; left: 704px; top: 150px;
    font-family: "Varela Round", sans-serif; font-size: 24px; color: var(--ink);
  }
  .product-title {
    position: absolute; left: 37px; top: 206px;
    font-family: "Barlow Semi Condensed", sans-serif; font-weight: 500;
    font-size: 30px; line-height: 39px; text-transform: uppercase; color: var(--ink);
  }
  .feature-list {
    position: absolute; left: 34px; top: 310px; width: 780px;
    font-family: "Varela Round", sans-serif; font-size: 18.5px; line-height: 20.8px;
    list-style: none; color: var(--ink);
  }
  .feature-list li { padding-left: 18px; text-indent: -12px; }
  .feature-list li::before { content: "• "; }
  .pack-contents {
    position: absolute; left: 36px; top: 547px;
    font-family: "Barlow Semi Condensed", sans-serif; font-weight: 600;
    font-size: 16.5px; color: var(--ink);
  }
  .badge {
    position: absolute; width: 130px; text-align: center;
    font-family: "Barlow", sans-serif; font-weight: 600; font-size: 15.5px; color: var(--leaf-green);
  }
  .badge svg { display: block; margin: 0 auto 6px; }
  .badge--natural { left: 804px; top: 194px; }
  .badge--biodegradable { left: 804px; top: 313px; }
  .badge--eco { left: 804px; top: 431px; }
</style>
</head>
<body>
  <div class="foliage-backdrop" role="img" aria-label="Tropical palm fronds in teal and mint green on a dark background"></div>

  <section class="label-card">
    <div class="brand-name">Velmorani</div>
    <div class="brand-parent">By Quorvel</div>

    <h1 class="product-title">Deluxe Palm Leaf Plates<br>Set of 25 Square Plates - 10 Inches – 25 cm x 25 cm</h1>

    <ul class="feature-list">
      <li>Made from naturally fallen Areca palm leaves – 100% natural without any chemicals</li>
      <li>No trees were harmed in the production of these plates</li>
      <li>Biodegradable - After use can be turned to a good source of organic manure</li>
      <li>Ideally suited for any celebration</li>
      <li>100% GUARANTEE - if for any reason you are not happy with our eco-friendly palm leaf plates, simply contact us within 30 days for a full refund or replacement.</li>
      <li>To reach our customer service team you can call: 03335550172</li>
    </ul>

    <p class="pack-contents">25 pcs - 10'' Square (25 cm) + 10 pcs – 6'' Square (15 cm) | 100% Palm Leaf | Plates Made in India</p>

    <div class="badge badge--natural">
      <svg width="88" height="88" viewBox="0 0 88 88" role="img" aria-label="Leaf icon">
        <circle cx="44" cy="44" r="42" fill="var(--badge-fill)" stroke="var(--badge-line)" stroke-width="2"/>
        <path d="M24 60 C24 34 44 22 66 24 C66 48 50 62 24 60 Z" fill="var(--badge-line)"/>
        <path d="M24 60 L58 32" stroke="var(--badge-fill)" stroke-width="2.5"/>
      </svg>
      100% Natural
    </div>
    <div class="badge badge--biodegradable">
      <svg width="88" height="88" viewBox="0 0 88 88" role="img" aria-label="Recycling globe icon">
        <circle cx="44" cy="44" r="42" fill="var(--badge-fill)" stroke="var(--badge-line)" stroke-width="2"/>
        <circle cx="44" cy="44" r="16" fill="none" stroke="var(--badge-line)" stroke-width="3"/>
        <path d="M22 38 A23 23 0 0 1 58 24 M66 50 A23 23 0 0 1 32 66" fill="none" stroke="var(--badge-line)" stroke-width="5" stroke-linecap="round"/>
      </svg>
      Biodegradable
    </div>
    <div class="badge badge--eco">
      <svg width="88" height="88" viewBox="0 0 88 88" role="img" aria-label="Tree held in hands icon">
        <circle cx="44" cy="44" r="42" fill="var(--badge-fill)" stroke="var(--badge-line)" stroke-width="2"/>
        <circle cx="44" cy="34" r="16" fill="var(--badge-line)"/>
        <path d="M44 40 V62 M22 62 Q44 74 66 62" stroke="var(--badge-line)" stroke-width="4" fill="none" stroke-linecap="round"/>
      </svg>
      Eco-Friendly
    </div>
  </section>
</body>
</html>
```